Professional/Sleek card design for athletic apparel brand

Athletic apparel brand. Mainly focused on lifting weights/gym workouts. Logo and brand are already created. Must use brand logo and name. Creativity is welcome. Looking for a clean, modern, and sexy design.

```html
<!DOCTYPE html>
<html lang="en">
<head>
<meta charset="UTF-8">
<title>Iron and Grit – Business Card</title>
<link href="https://fonts.googleapis.com/css2?family=Montserrat:wght@300;400;600;700&display=swap" rel="stylesheet">
<style>
  :root {
    --backdrop: #1b1b1c;
    --card: #0e0e0e;
    --ink: #f2f2f2;
    --ink-soft: #d6d6d6;
  }
  * { margin: 0; padding: 0; box-sizing: border-box; }
  html, body {
    width: 1200px; height: 800px; overflow: hidden;
    background: var(--backdrop);
    font-family: "Montserrat", sans-serif;
    color: var(--ink);
  }
  .stage {
    position: relative; width: 1200px; height: 800px;
    display: flex; align-items: center; justify-content: center; gap: 60px;
  }
  .card {
    position: relative; width: 500px; height: 286px;
    background: var(--card); border-radius: 18px; overflow: hidden;
    box-shadow: 0 18px 40px rgba(0,0,0,.45);
  }
  /* front */
  .card--front {
    display: flex; flex-direction: column; align-items: center; justify-content: center; gap: 22px;
  }
  .brand-dot {
    width: 34px; height: 34px; border-radius: 50%; background: var(--ink);
  }
  .brand-name {
    font-weight: 600; font-size: 20px; letter-spacing: 0.55em;
    text-transform: uppercase; padding-left: 0.55em;
  }
  /* back */
  .card--back { padding: 70px 0 0 48px; }
  .holder-name { font-weight: 700; font-size: 22px; letter-spacing: 0.01em; text-transform: uppercase; }
  .holder-role { font-weight: 300; font-size: 13px; letter-spacing: 0.04em; text-transform: uppercase; margin: 2px 0 0 8px; color: var(--ink-soft); }
  .contact-list { list-style: none; margin: 26px 0 0 30px; }
  .contact-list li { font-weight: 300; font-size: 15px; line-height: 1.75; color: var(--ink-soft); }
  .address { margin: 14px 0 0 38px; font-weight: 400; font-size: 11px; line-height: 1.35; color: var(--ink-soft); }
  .card-accent {
    position: absolute; right: -70px; top: -10px;
    width: 240px; height: 300px;
  }
</style>
</head>
<body>
<main class="stage">
  <section class="card card--front" aria-label="Card front">
    <span class="brand-dot"></span>
    <p class="brand-name">Iron and Grit</p>
  </section>

  <section class="card card--back" aria-label="Card back">
    <h1 class="holder-name">Marcus Delane</h1>
    <p class="holder-role">Founder</p>
    <ul class="contact-list">
      <li>P:&nbsp; +123 456 789</li>
      <li>M: info@yourname.com</li>
      <li>W: www.websitename.com</li>
    </ul>
    <p class="address">123, Avenue, Street,<br>Your City, County, Postal Code</p>
    <svg class="card-accent" viewBox="0 0 240 300" aria-hidden="true">
      <circle cx="120" cy="160" r="120" fill="var(--ink)"/>
    </svg>
  </section>
</main>
</body>
</html>
```